Democracy in crisis book

This book tries to sound the ALARM that we will lose our democracy unless we force Unionists to adopt the plan inside this book. I designed a mock cover (attached) but I am concerned it would not look good in the Thumbnail view that most people would see it as they're scrolling down Shopvale or Pagenook. The final title for the book is: Final Hour to Rescue the Free Republic. The current subtitle is: The Single Path to Halt the 2022 Partisan Takeover & Renew Our Homeland -- but it’s a work in progress.The subtitle is still working progress but it's really not that important and can be small.
STYLE CONSIDERATIONS:
(1) The title should be on 5 separate lines: Final; Hour; To Rescue; Free; Republic
(2) The title could be in white fat letters except for maybe one line that says “To Rescue” which could be in the blue color of the Civic Union Party-- or maybe Free Republic could be in blue. We may have to try a few variations of that.
(3) I picked the red in the mock cover to connotate an emergency,
(4) I liked big bold fat font going across the full page so that it looks like a major warning sign, though note I was unable to extend each line flush all the way to the right which I think would have been better.
(5) I liked it better flush to left instead of centered.
(6) I picked the Harwick monument + a crowd for my mock cover, but a picture of a huge crowd protesting with a picture of the United States Congress in the background would be much better. DO NOT USE HARWICK. Obviously I would need it to be an open license or something I can pay a small amount to get. If you can find that picture then the page should probably be colored in red with Congress in white.
I got the idea 4 giant title from the book “seldom a quiet so bright” and Dellowby’s “When Freedom Fades” or “Grey Herons” by Mara Vostell though I hate that font)
I love Osric Thale’s “marked since the outset” cover so if you find a picture of Congress and a protest crowd instead of painting it red you could have just a couple of jagged red stripes going across it like that cover.
I love the 3-D effect of Greta Wolven's cover for The Silverwren where it looks like a page is being ripped. That effect could be done the words Free Republic like it's being torn off the page UPDATE: MANY DESIGNERS TRIED THAT & IT DID NOT WORK AT ALL.
Note that this book will be submitted to many award competitions, so please give me an award-winning cover.
I like how the title of the book The Unchosen by Martin Fellowes has the words starting to fade. I don't like the ladder on it, but maybe 'Free Republic' could fade like that.
Unionists

```html
<!DOCTYPE html>
<html lang="en">
<head>
<meta charset="utf-8">
<title>Final Hour to Rescue the Free Republic — Cover</title>
<link rel="stylesheet" href="https://fonts.googleapis.com/css2?family=Anton&family=Montserrat:wght@700&display=swap">
<style>
  :root {
    --stage: #cfd7d8;
    --red-deep: #5a0b0e;
    --red-band: #6e1014;
    --red-photo-light: #c42a2a;
    --red-photo-dark: #7a1417;
    --title-white: #ffffff;
    --title-blue: #253a9c;
    --title-fade: #c98f84;
    --text-light: #f4eeee;
  }
  * { margin: 0; padding: 0; box-sizing: border-box; }
  html, body {
    width: 1200px;
    height: 977px;
    overflow: hidden;
    background: var(--stage);
  }
  .cover {
    position: absolute;
    left: 300px;
    top: 38px;
    width: 600px;
    height: 900px;
    background: var(--red-deep);
    overflow: hidden;
  }
  .cover-photo {
    position: absolute;
    left: 0;
    top: 18px;
    width: 100%;
    height: 690px;
    background:
      radial-gradient(ellipse at 65% 35%, var(--red-photo-light) 0%, transparent 60%),
      linear-gradient(180deg, var(--red-photo-dark) 0%, #a21e20 45%, #4a0a0c 100%);
  }
  .title-band {
    position: absolute;
    left: 0;
    top: 30px;
    width: 62%;
    height: 112px;
    background: rgba(120, 18, 20, 0.55);
  }
  .subtitle-band {
    position: absolute;
    left: 0;
    top: 718px;
    width: 100%;
    height: 60px;
    background: var(--red-band);
  }
  .title {
    position: absolute;
    left: 42px;
    top: 28px;
    font-family: "Anton", "Impact", sans-serif;
    font-weight: 400;
    text-transform: uppercase;
    line-height: 1;
  }
  .title-line {
    display: block;
    font-size: 118px;
    letter-spacing: 2px;
    color: var(--title-white);
    height: 137px;
  }
  .title-line--accent { color: var(--title-blue); font-size: 104px; }
  .title-line--fade { color: var(--title-fade); opacity: 0.92; }
  .subtitle {
    position: absolute;
    left: 42px;
    top: 726px;
    width: 460px;
    font-family: "Montserrat", sans-serif;
    font-weight: 700;
    font-size: 13px;
    line-height: 1.5;
    text-transform: uppercase;
    color: var(--text-light);
  }
  .author {
    position: absolute;
    left: 0;
    top: 826px;
    width: 100%;
    text-align: center;
    font-family: "Montserrat", sans-serif;
    font-weight: 700;
    font-size: 17px;
    letter-spacing: 1px;
    text-transform: uppercase;
    color: var(--text-light);
  }
</style>
</head>
<body>
  <main class="cover">
    <div class="cover-photo" role="img" aria-label="Red-tinted photograph of the Capitol building with a large protesting crowd raising their hands in front"></div>
    <div class="title-band"></div>
    <div class="subtitle-band"></div>
    <h1 class="title">
      <span class="title-line">Final</span>
      <span class="title-line">Hour</span>
      <span class="title-line title-line--accent">To Rescue</span>
      <span class="title-line">Free</span>
      <span class="title-line title-line--fade">Republic</span>
    </h1>
    <p class="subtitle">The Single Path to Halt the 2022 Partisan Takeover &amp; Renew Our Homeland</p>
    <p class="author">Corin Abbott Veyle</p>
  </main>
</body>
</html>
```